Criação de Papelaria Profissional para Consultoria de Negócios
" Somos uma empresa de consultoria para transportadoras, atuamos de forma operacional, fazemos um diagnóstico dos problemas da empresa, desenhamos processos, treinamos e auditamos o andamento, atuamos em todas os departamentos de uma transportadora. "

```html
<!DOCTYPE html>
<html lang="pt-BR">
<head>
<meta charset="UTF-8">
<title>Vertra Consultoria — Papelaria</title>
<link href="https://fonts.googleapis.com/css2?family=Nunito:wght@400;600;900&display=swap" rel="stylesheet">
<style>
  :root {
    --stage: #e6e7ea;
    --paper: #ffffff;
    --paper-shade: #eef0f2;
    --brand-blue: #1d6fb5;
    --brand-blue-light: #3fa2e0;
    --brand-orange: #f58a1f;
    --ink: #4a4f57;
    --ink-soft: #7b818a;
  }
  * { box-sizing: border-box; margin: 0; padding: 0; }
  html, body { width: 1200px; height: 1200px; overflow: hidden; }
  body {
    background: var(--stage);
    font-family: "Nunito", Arial, sans-serif;
    position: relative;
  }
  .profile-card {
    position: absolute;
    left: 475px; top: 137px;
    width: 198px; height: 198px;
    background: var(--paper);
    box-shadow: 0 6px 18px rgba(0,0,0,.18);
    display: flex; align-items: center; justify-content: center;
  }
  .profile-card .brand-name {
    font-weight: 900; font-size: 36px; color: var(--brand-blue);
  }
  .cover {
    position: absolute;
    left: 24px; top: 437px;
    width: 1152px; height: 470px;
    background: linear-gradient(180deg, var(--paper) 0%, var(--paper-shade) 100%);
    box-shadow: 0 8px 24px rgba(0,0,0,.2);
    overflow: hidden;
  }
  .cover .puzzle-art { position: absolute; left: 0; top: 24px; }
  .cover .brand {
    position: absolute; left: 500px; top: 150px;
    display: flex; align-items: center; gap: 22px;
  }
  .cover .brand-dot {
    width: 96px; height: 96px; border-radius: 50%;
    background: var(--brand-orange);
  }
  .cover .brand-text { display: flex; flex-direction: column; line-height: 1; }
  .cover .brand-name { font-weight: 900; font-size: 92px; color: var(--brand-blue); }
  .cover .brand-tagline {
    font-weight: 900; font-size: 26px; color: var(--brand-blue);
    letter-spacing: 3px; margin-top: 4px;
  }
  .cover .contact {
    position: absolute; left: 540px; top: 308px;
    width: 340px; text-align: center; color: var(--ink);
  }
  .cover .contact .site { font-size: 22px; font-weight: 600; }
  .cover .contact .phones { font-size: 14px; margin-top: 10px; color: var(--ink-soft); }
  .cover .social {
    position: absolute; right: 36px; top: 404px;
    font-size: 13px; color: var(--ink-soft);
  }
  .cover .footer-band {
    position: absolute; left: 0; right: 0; top: 432px; height: 16px;
    background: linear-gradient(90deg, var(--brand-blue) 0%, var(--brand-blue-light) 100%);
  }
</style>
</head>
<body>
  <section class="profile-card">
    <span class="brand-name">Vertra</span>
  </section>

  <section class="cover">
    <svg class="puzzle-art" width="400" height="408" viewBox="0 0 400 408"
         role="img" aria-label="Ilustração de quebra-cabeça em quatro peças coloridas com ícones de documento, engrenagens, gráfico e pessoa em movimento">
      <defs>
        <linearGradient id="puzzleTones" x1="0" y1="0" x2="1" y2="1">
          <stop offset="0" stop-color="#f7b23b"/>
          <stop offset=".45" stop-color="#e8404f"/>
          <stop offset="1" stop-color="#1f8a8c"/>
        </linearGradient>
      </defs>
      <path d="M0 0 H190 A204 204 0 0 1 190 408 H0 Z" fill="url(#puzzleTones)"/>
    </svg>

    <div class="brand">
      <span class="brand-dot"></span>
      <div class="brand-text">
        <span class="brand-name">Vertra</span>
        <span class="brand-tagline">CONSULTORIA</span>
      </div>
    </div>

    <div class="contact">
      <p class="site">www.vertraconsultoria.com.br</p>
      <p class="phones">(xx) xxxx-xxx &nbsp;&nbsp; (xx) xxxx-xxx</p>
    </div>

    <p class="social">/vertraconsultoria</p>
    <div class="footer-band"></div>
  </section>
</body>
</html>
```